Design a cover that embodies the concept of healing by Walking Out of the Fog

Subtitle: How to use tapping, applied kinesiology, and Chinese medicine to heal your body, free your mind and live in peace.

Tapping (Emotional Freedom Technique) is a modern mix of psychology and Chinese medicine that helps people to release the emotions they have inside that are contributing to the depression and anxiety they feel. Applied kinesiology or muscle testing is a biofeedback tool which helps to extract information from the body that can help people to profoundly heal. It can be used to determine whether heavy metals, heavy chemicals, food sensitivities or pathogens are causing the body problems. It can also be used to determine which supplements can help someone heal. This tool also can be used to identify emotions and memories that are also causing someone problems. Lastly, Chinese medicine uses food therapy, herbal formulas, meditation, tai chi (meditative movement), cupping and other tools to help people to be free of depression. This book is written to be information but also details my own personal journey of how I was able to heal from 11 years of heavy depression through the use of these tools.

The heart of the book is about emotional release, emotional freedom and emotional healing. You can surrender, release or let go of emotions and feel better very quickly. This certainly was my experience.

I would like the front and back cover to each be 8.5" x 5.5". I still have to get an ISBN number for the back page as well. Here is the text that I would like on the back cover for now: Millions of people feel the pain, loneliness, and agony of anxiety and depression every day. Many turn to Western medicine in the hopes that a pill will ease the pain and make the problem go away. Oftentimes, this only makes matters worse and doesn’t address the root cause. No one should have to struggle like this when natural answers exist that can address the physical, energetic, emotional, or spiritual causes of anxiety and depression. For 11 long years, Dr. Vance personally struggled with heavy depression until he discovered answers that helped him to completely heal. Walking Out of the Fog is a guide that will help you discover - The two root physical causes of depression and exactly what to do to start healing today - How the negative emotions we have stored within from trauma and bad experiences can drive depression - Tools from Chinese medicine, applied kinesiology, and tapping to help you free your mind and live in peace - An actionable plan to help you let go of the pain, suffering, and negative emotions from your past Whether you feel depressed and anxious or know someone who struggles with these issues, Walking Out of the Fog will transform how you think about depression and will give you the tools to heal so that you can be free and live in peace. Dr. Vance Holbrook is a board-certified acupuncture physician licensed in the state of Florida. He received his training at the Calder Institute of Holistic Practice. He also graduated with a master’s degree in counseling and psychology from Meadowbrook Seminary of Theology. His mission is to help people transform their health and improve the quality of their life naturally. He lives in Orlando, FL where he runs a holistic medical clinic called Bluepine Wellness Center. www.drvanceholbrook-example.com Instagram: drvanceholbrook Facebook: bluepinewellnesscenter

Target Market(s)

Those who suffer from depression and anxiety and want to heal naturally

Industry/Entity Type

Health And Wellness

Requirements
Must have
• My picture should be small and go on the back cover next to the information about me. The front cover would be all graphical. Thank you. On the front cover my name should be posted as "Dr. Vance Holbrook, AP, MA"

```html
<!DOCTYPE html>
<html lang="en">
<head>
<meta charset="utf-8">
<title>Walking Out of the Fog – Cover Spread</title>
<link href="https://fonts.googleapis.com/css2?family=Arimo:ital,wght@0,400;0,700;1,700&family=Dancing+Script:wght@500&display=swap" rel="stylesheet">
<style>
  :root {
    --backdrop: #bfb4aa;
    --cream: #fdf9ec;
    --cream-warm: #f8efd6;
    --gold: #f6c21a;
    --gold-rule: #f2b705;
    --ink: #111111;
    --body-ink: #1c1c1c;
    --sun-glow: #fff4d2;
    --sand: #b89b7a;
    --sea: #8c7a67;
    --parchment: #d8b98c;
    --portrait: #c9a88a;
  }
  * { box-sizing: border-box; margin: 0; padding: 0; }
  html, body { width: 852px; height: 1200px; overflow: hidden; }
  body {
    background: var(--backdrop);
    font-family: "Arimo", Arial, sans-serif;
    position: relative;
  }
  .spread {
    position: absolute;
    left: 20px; top: 300px;
    width: 812px; height: 600px;
    background: linear-gradient(180deg, var(--cream) 0%, var(--cream-warm) 48%, var(--sun-glow) 58%);
    box-shadow: 0 6px 14px rgba(0,0,0,.35);
    overflow: hidden;
  }
  .beach-photo {
    position: absolute;
    left: 0; right: 0; top: 330px; bottom: 0;
    background:
      radial-gradient(ellipse 260px 120px at 560px 70px, #fffbe8 0%, rgba(255,244,205,.6) 45%, rgba(255,244,205,0) 100%),
      linear-gradient(180deg, var(--sun-glow) 0%, #efd9ac 40%, var(--sand) 70%, var(--sea) 100%);
  }
  .back-cover { position: absolute; left: 0; top: 0; width: 381px; height: 600px; padding: 22px 28px 0 28px; }
  .spine { position: absolute; left: 381px; top: 0; width: 46px; height: 600px; }
  .front-cover { position: absolute; left: 427px; top: 0; width: 385px; height: 600px; }

  .title-gold { color: var(--gold); }
  .title-ink { color: var(--ink); }

  .back-title { font-weight: 700; font-size: 25px; line-height: 1; margin-bottom: 12px; white-space: nowrap; }
  .back-copy { font-size: 10.2px; line-height: 1.18; color: var(--body-ink); text-align: justify; }
  .back-copy p { margin-bottom: 11px; }
  .benefits { list-style: none; text-align: left; }
  .benefits li { position: relative; padding-left: 7px; }
  .benefits li::before {
    content: ""; position: absolute; left: 0; top: 4px;
    width: 4px; height: 4px; border-radius: 50%; background: var(--gold);
  }
  .gold-rule { height: 2px; width: 205px; margin: 14px 0 18px 68px; background: linear-gradient(90deg, rgba(242,183,5,0), var(--gold-rule) 30%, var(--gold-rule) 70%, rgba(242,183,5,0)); }
  .author-bio { font-size: 10.2px; line-height: 1.18; color: var(--body-ink); text-align: justify; }
  .author-portrait {
    float: left; width: 68px; height: 68px; margin: 0 12px 2px 0;
    background: linear-gradient(160deg, #e7d6c0, var(--portrait));
  }
  .author-bio strong { font-style: italic; }
  .contact-list {
    position: absolute; left: 28px; top: 522px;
    font-size: 10.4px; font-weight: 700; line-height: 1.55; color: var(--ink);
  }
  .isbn-box { position: absolute; left: 250px; top: 514px; width: 100px; height: 61px; background: #ffffff; }

  .spine-text {
    position: absolute; left: 50%; transform: translateX(-50%);
    writing-mode: vertical-rl; white-space: nowrap;
  }
  .spine-title { top: 24px; font-weight: 700; font-size: 21px; }
  .spine-author { top: 372px; font-size: 14px; color: var(--ink); }

  .front-author { position: absolute; left: 0; right: 0; top: 18px; text-align: center; font-size: 18px; color: var(--ink); }
  .front-title { position: absolute; left: 52px; top: 62px; font-weight: 700; line-height: 1.02; }
  .front-title .line-one { display: block; font-size: 37px; }
  .front-title .line-two { display: block; font-size: 48px; }
  .front-subtitle {
    position: absolute; left: 52px; top: 160px; width: 196px;
    font-family: "Dancing Script", cursive; font-size: 15.5px; line-height: 1.15; color: var(--ink);
  }
  .hand-art {
    position: absolute; left: 262px; top: 150px; width: 104px; height: 190px;
    background: linear-gradient(170deg, #e6cea6, var(--parchment));
    border-radius: 36px 36px 50px 50px;
    opacity: .92;
  }
</style>
</head>
<body>
  <main class="spread">
    <div class="beach-photo" role="img" aria-label="Photograph of a woman in a white dress with arms raised on a beach at sunrise, golden light over the sea"></div>

    <section class="back-cover">
      <h2 class="back-title"><span class="title-gold">Walking Out of</span> <span class="title-ink">the Fog</span></h2>
      <div class="back-copy">
        <p>Millions of people feel the pain, loneliness, and agony of anxiety and depression every day. Many turn to Western medicine in the hopes that a pill will ease the pain and make the problem go away. Oftentimes, this only makes matters worse and doesn’t address the root cause. No one should have to struggle like this when natural answers exist that can address the physical, energetic, emotional, or spiritual causes of anxiety and depression.</p>
        <p>For 11 long years, Dr. Vance personally struggled with heavy depression until he discovered answers that helped him to completely heal. Walking Out of the Fog is a guide that will help you discover:</p>
        <ul class="benefits">
          <li>The two root physical causes of depression and exactly what to do to start healing today</li>
          <li>How the negative emotions we have stored within from trauma and bad experiences can drive depression</li>
          <li>Tools from Chinese medicine, applied kinesiology, and tapping to help you free your mind and live in peace</li>
          <li>An actionable plan to help you let go of the pain, suffering, and negative emotions from your past</li>
        </ul>
        <p style="margin-top:11px">Whether you feel depressed and anxious or know someone who struggles with these issues, Walking Out of the Fog will transform how you think about depression and will give you the tools to heal so that you can be free and live in peace.</p>
      </div>
      <div class="gold-rule"></div>
      <div class="author-bio">
        <div class="author-portrait" role="img" aria-label="Small portrait photo of the author"></div>
        <strong>Dr. Vance Holbrook</strong> is a board-certified acupuncture physician licensed in the state of Florida. He received his training at the Calder Institute of Holistic Practice. He also graduated with a master’s degree in counseling and psychology from Meadowbrook Seminary of Theology. His mission is to help people transform their health and improve the quality of their life naturally. He lives in Orlando, FL where he runs a holistic medical clinic called Bluepine Wellness Center.
      </div>
      <div class="contact-list">
        <div>www.drvanceholbrook-example.com</div>
        <div>Instagram: drvanceholbrook</div>
        <div>Facebook: bluepinewellnesscenter</div>
      </div>
      <div class="isbn-box"></div>
    </section>

    <section class="spine">
      <div class="spine-text spine-title"><span class="title-gold">Walking Out of</span> <span class="title-ink">the Fog</span></div>
      <div class="spine-text spine-author">Dr. Vance Holbrook, AP, MA</div>
    </section>

    <section class="front-cover">
      <div class="front-author">Dr. Vance Holbrook, AP, MA</div>
      <h1 class="front-title">
        <span class="line-one title-gold">Walking Out of</span>
        <span class="line-two title-ink">the Fog</span>
      </h1>
      <p class="front-subtitle">How to use tapping, applied kinesiology, and Chinese medicine to heal your body, free your mind and live in peace.</p>
      <div class="hand-art" role="img" aria-label="Illustration of a raised hand made of aged parchment printed with Chinese characters"></div>
    </section>
  </main>
</body>
</html>
```